Garage Flooring Flyer

We are looking for a flyer design for our garage flooring company. We specialise in installing garage floor coatings. We use industrial grade products and are serious about durability and quality.
We target male car enthusiasts and want to project the image of a modern high-tech company. The flyer should be stunningly visual and incorporate the logo and photos we have attached. Other photos or images are welcomed.
Some key mentions to be made on the flyer are listed below:
About Us
"We are K*** R***** LLC, Home of the garage enthusiasts and Waukesha’s premier garage floor installer"
Services
Garage Floor Coatings
Offers
-Call or Email for a FREE estimate!
Credentials
-QN logo
-Pictavo Logo
-Zorbin Logo
-5stars?
Benefit Highlights to be mentioned or listed (not in any particular order)
-Industrial Quality and Strength
-Easy to Clean
-Many Color Options
-Locally Owned and Operated
-Satisfaction Guaranteed
-Lifetime Limited Warranty
-Increases Home Value
-MAKE YOUR FRIENDS AND NEIGHBORS JEALOUS!
-Fully Insured
-Certified and Trusted Installer
-Oil and Chemical Resistant
-UV Stable
-Impact and Abrasion Resistant
Contact Info
-Phone
-Email
-Website
Captions
-"From diamond grinding surface prep to using only the highest industrial-grade products, we believe in taking the time to ensure a proper installation and guarantee a durable long-lasting and beautiful garage floor";
-Serving Southeastern Wisconsin!

```html
<!DOCTYPE html>
<html lang="en">
<head>
<meta charset="utf-8">
<title>Garage Floor Coatings Flyer</title>
<link href="https://fonts.googleapis.com/css2?family=Aldrich&display=swap" rel="stylesheet">
<style>
  :root {
    --backdrop: #7b97ab;
    --black: #060606;
    --deep: #0d0d0d;
    --strip: #161616;
    --silver: #b9bbbd;
    --grey-text: #a9a9a9;
    --white: #ffffff;
    --paper: #eeeeee;
    --ink: #151515;
    --speckle: #9c9c9c;
    --speckle-warm: #b9b1a1;
  }
  * { margin: 0; padding: 0; box-sizing: border-box; }
  html, body { width: 1200px; height: 931px; overflow: hidden; }
  body { background: var(--backdrop); font-family: "Aldrich", sans-serif; position: relative; }
  .page { position: absolute; top: 142px; width: 494px; height: 640px; overflow: hidden; }
  .page--front { left: 70px; background: var(--black); }
  .page--back { left: 629px; background: var(--paper); }
  .abs { position: absolute; }
  .center { left: 0; right: 0; text-align: center; }

  /* front */
  .front-photos { left: 0; top: 0; }
  .brand { top: 390px; color: var(--silver); text-transform: uppercase; }
  .brand__name { font-size: 46px; letter-spacing: 2px; line-height: 1; }
  .brand__suffix { font-size: 28px; letter-spacing: 26px; margin-top: 16px; padding-left: 26px; line-height: 1; }
  .tagline { top: 515px; color: var(--grey-text); text-transform: uppercase; }
  .tagline__small { font-size: 9.5px; }
  .tagline__large { font-size: 15px; margin-top: 2px; }
  .guarantee { top: 565px; color: var(--grey-text); font-size: 11px; text-transform: uppercase; }
  .stars { top: 580px; }
  .front-footer { left: 0; right: 0; top: 590px; bottom: 0; background: var(--deep); }
  .contact { left: 146px; width: 262px; top: 600px; border-top: 1px solid #666; padding-top: 3px;
             display: flex; justify-content: space-between; color: var(--silver); font-size: 6.3px; text-transform: uppercase; }

  /* back */
  .back-top { left: 0; top: 0; width: 494px; height: 212px; background: var(--black); }
  .headline { top: 28px; color: var(--silver); font-size: 18px; }
  .headline span { border-bottom: 1px solid var(--silver); padding-bottom: 1px; }
  .intro { top: 60px; left: 46px; right: 46px; color: var(--white); font-size: 7.6px; line-height: 14.5px;
           text-align: justify; text-align-last: center; text-transform: uppercase; letter-spacing: .3px; }
  .services { top: 134px; color: var(--white); font-size: 17px; font-weight: 700; text-shadow: 0 0 .5px #fff; }
  .services-line { top: 157px; color: var(--grey-text); font-size: 16px; }
  .texture-band { left: 0; top: 212px; }
  .benefits { top: 451px; left: 24px; right: 24px; display: flex; justify-content: space-between;
              font-size: 6.2px; color: var(--ink); text-transform: uppercase; line-height: 18.2px; }
  .benefits ul { list-style: none; }
  .benefits--right { text-align: right; }
  .cta { left: 118px; top: 523px; width: 258px; height: 45px; border: 2px solid var(--ink);
         text-align: center; color: var(--ink); text-transform: uppercase; padding-top: 5px; }
  .cta__lead { font-size: 11px; line-height: 13px; }
  .cta__offer { font-size: 16.5px; line-height: 20px; text-shadow: 0 0 .4px var(--ink); }
  .region { top: 589px; color: var(--ink); font-size: 14px; text-transform: uppercase; }
  .region-rule { left: 116px; width: 262px; top: 609px; border-top: 1px solid var(--ink); }
  .socials { top: 617px; display: flex; justify-content: center; gap: 8px; color: var(--ink); font-size: 7px; text-transform: uppercase; }
  .socials span::before { content: ""; display: inline-block; width: 5px; height: 5px; background: var(--ink); margin-right: 3px; vertical-align: 0; }
</style>
</head>
<body>

<section class="page page--front" aria-label="Flyer front">
  <svg class="abs front-photos" width="494" height="340" viewBox="0 0 494 340">
    <defs>
      <linearGradient id="garageTop" x1="0" y1="0" x2="0" y2="1">
        <stop offset="0" stop-color="#c6c8ca"/><stop offset=".55" stop-color="#a9abad"/><stop offset="1" stop-color="#8f9294"/>
      </linearGradient>
      <linearGradient id="garageBottom" x1="0" y1="0" x2="1" y2="1">
        <stop offset="0" stop-color="#8ea3b6"/><stop offset=".5" stop-color="#6f8599"/><stop offset="1" stop-color="#4d6174"/>
      </linearGradient>
    </defs>
    <polygon points="0,0 494,0 494,150 345,152 0,218" fill="url(#garageTop)" role="img" aria-label="Photo of a white sports car on a lift in a speckled-floor garage"/>
    <polygon points="0,218 345,152 494,150 494,160 350,162 0,228" fill="#ffffff"/>
    <polygon points="0,228 350,162 494,160 494,340 0,340" fill="url(#garageBottom)" role="img" aria-label="Low-angle photo of a silver sports car on a coated garage floor"/>
  </svg>
  <div class="abs" style="left:0;top:340px;width:494px;height:16px;background:var(--strip)"></div>

  <div class="abs center brand">
    <div class="brand__name">K*** R*****</div>
    <div class="brand__suffix">LLC</div>
  </div>

  <div class="abs center tagline">
    <div class="tagline__small">Home of the garage enthusiasts and Waukesha's</div>
    <div class="tagline__large">Premier garage floor installer</div>
  </div>

  <div class="front-footer abs"></div>
  <div class="abs center guarantee">Satisfaction Guaranteed</div>
  <svg class="abs stars" style="left:211px" width="74" height="12" viewBox="0 0 74 12" aria-label="Five stars">
    <g fill="#ffffff">
      <polygon id="star" points="5,0 6.2,3.8 10,3.8 6.9,6.1 8.1,10 5,7.6 1.9,10 3.1,6.1 0,3.8 3.8,3.8"/>
      <use href="#star" x="16"/><use href="#star" x="32"/><use href="#star" x="48"/><use href="#star" x="64"/>
    </g>
  </svg>
  <div class="abs contact">
    <span>(262) 555-0148</span><span>www.kestrelfloors.com</span><span>hello@kestrelfloors.com</span>
  </div>
</section>

<section class="page page--back" aria-label="Flyer back">
  <div class="abs back-top"></div>
  <div class="abs center headline"><span>INCREASE YOUR HOME VALUE</span></div>
  <p class="abs intro">From diamond grinding surface prep to using only the highest industrial-grade products, we believe in taking the time to ensure a proper installation and guarantee a durable long-lasting and beautiful garage floor</p>
  <div class="abs center services">SERVICES</div>
  <div class="abs center services-line">GARAGE FLOOR COATINGS</div>

  <svg class="abs texture-band" width="494" height="222" viewBox="0 0 494 222">
    <defs>
      <linearGradient id="floorGrey" x1="0" y1="0" x2="1" y2="1">
        <stop offset="0" stop-color="#a3a5a8"/><stop offset="1" stop-color="#8d8f92"/>
      </linearGradient>
      <linearGradient id="floorWarm" x1="0" y1="0" x2="1" y2="0">
        <stop offset="0" stop-color="#a8a7a3"/><stop offset="1" stop-color="#c2b89f"/>
      </linearGradient>
      <radialGradient id="carShot" cx=".5" cy=".55" r=".6">
        <stop offset="0" stop-color="#2a2a2c"/><stop offset=".7" stop-color="#101012"/><stop offset="1" stop-color="#6f7073"/>
      </radialGradient>
    </defs>
    <rect x="0" y="0" width="494" height="90" fill="url(#floorGrey)" role="img" aria-label="Close-up of grey flake floor coating"/>
    <rect x="0" y="90" width="494" height="30" fill="#0a0a0a"/>
    <rect x="0" y="120" width="247" height="90" fill="url(#floorGrey)" role="img" aria-label="Close-up of speckled floor coating"/>
    <rect x="247" y="120" width="247" height="90" fill="url(#floorWarm)" role="img" aria-label="Close-up of beige flake floor coating"/>
    <rect x="0" y="210" width="494" height="12" fill="var(--paper)"/>
    <polygon points="247,-26 377,103 247,232 117,103" fill="#0a0a0a"/>
    <polygon points="247,-8 359,103 247,214 135,103" fill="url(#carShot)" role="img" aria-label="Photo of a black supercar wheel on a glossy coated floor"/>
  </svg>

  <div class="abs benefits">
    <ul>
      <li>&lt;&gt; Easy to clean &nbsp;•&nbsp; Many color options</li>
      <li>&lt;&gt; Impact and abrasion resistant</li>
      <li>&lt;&gt; Oil and chemical resistant &nbsp;•&nbsp; UV stable - won't yellow</li>
    </ul>
    <ul class="benefits--right">
      <li>Industrial quality and strength &lt;&gt;</li>
      <li>Locally owned and operated &lt;&gt;</li>
      <li>Fully insured &nbsp;•&nbsp; Certified and trusted installer &lt;&gt;</li>
    </ul>
  </div>

  <div class="abs cta">
    <div class="cta__lead">Call or email for a</div>
    <div class="cta__offer">Free estimate!</div>
  </div>

  <div class="abs center region">Serving Southeastern Wisconsin!</div>
  <div class="abs region-rule"></div>
  <div class="abs center socials"><span>Zorbin</span><span>QN</span><span>Pictavo</span></div>
</section>

</body>
</html>
```